Complete web design based around only our company logo

I need someone to build a web page based around our company logo. I will provide other sites that we like and would want our site to be similar to.
Updates

Please look at these websites to get an idea of our industry

harlow minerals
pel minerals
fenwick royalty
tillamore energy
marlo energy

Our company buys mineral rights, and royalties from mineral owners all over the united states.  We also lease minerals as well. 

What we are trying to have designed is a fully functioning website that you upload to our webhost after we approve of final design.  

Target Market(s)

Oil and Gas/Mineral Owners

Industry/Entity Type

It Company

Font styles to use
Serif
Sans Serif

Colors
9ccb3b

Requirements
Must have
• Quick Contact form

```html
<!DOCTYPE html>
<html lang="en">
<head>
<meta charset="utf-8">
<title>Northgate Resources</title>
<link rel="stylesheet" href="https://fonts.googleapis.com/css2?family=Roboto:wght@400;500&family=Open+Sans:ital,wght@0,400;1,400&family=Arimo:wght@400;700&display=swap">
<style>
:root{
  --green-dark:#3a7d0f;
  --green-light:#9ccb3b;
  --text-dark:#1a1a1a;
  --text-body:#555;
  --text-muted:#777;
  --orange:#ea6136;
  --panel-grey:#e6e6e6;
  --footer-bg:#1f2227;
  --white:#fff;
}
*{margin:0;padding:0;box-sizing:border-box}
html,body{width:1161px;height:1200px;overflow:hidden;background:var(--white)}
body{position:relative;font-family:"Arimo",Arial,sans-serif;color:var(--text-dark)}
.abs{position:absolute}

.top-stripe{left:0;top:0;width:1161px;height:8px;background:var(--green-dark)}
.header{left:0;top:8px;width:1161px;height:131px;background:var(--white)}
.brand{left:194px;top:92px;display:flex;align-items:center;gap:8px;font-family:"Arimo",Arial,sans-serif;font-weight:700;font-size:17px;letter-spacing:.5px;color:var(--green-dark)}
.brand-mark{width:14px;height:14px;background:var(--green-dark)}
.phone{left:826px;top:64px;display:flex;align-items:center;gap:4px;font-size:14px;color:var(--text-dark)}

.nav{left:0;top:139px;width:1161px;height:57px;background:var(--green-light);border-top:2px solid #8ab834}
.nav a{position:absolute;top:24px;font-size:10px;color:var(--text-dark);text-decoration:none;white-space:nowrap}

.hero{left:0;top:196px;width:1161px;height:426px;background:linear-gradient(180deg,#d9d5cc 0%,#cfc3b0 45%,#c79a6a 80%,#d3895a 100%)}
.hero-shadow{left:230px;top:196px;width:700px;height:22px;background:radial-gradient(ellipse at 50% 0%,rgba(0,0,0,.35),rgba(0,0,0,0) 70%)}
.arrow{top:376px}
.dots{left:534px;top:579px;display:flex;gap:6px}
.dots span{width:8px;height:8px;border-radius:50%;background:var(--white)}
.dots span.active{background:#c477a7}

.quick-contact{left:676px;top:291px;width:288px;height:244px;background:rgba(255,255,255,.28);box-shadow:0 0 4px rgba(0,0,0,.08)}
.quick-contact h2{position:absolute;left:0;top:18px;width:100%;text-align:center;font-size:14px;font-weight:700;color:var(--green-dark)}
.qc-rule{position:absolute;left:40px;top:42px;width:202px;height:1px;background:rgba(90,90,90,.45)}
.field{position:absolute;left:22px;width:245px;height:32px;background:var(--white);border:1px solid #cfcfcf;font-size:10px;color:#666;padding:11px 10px}
.send{position:absolute;left:190px;top:195px;width:75px;height:32px;border-radius:5px;background:var(--green-dark);color:var(--white);font-weight:700;font-size:11px;text-align:center;line-height:32px;box-shadow:0 2px 2px rgba(0,0,0,.25)}

.about-title{left:194px;top:642px;font-family:"Roboto",sans-serif;font-size:19px;color:var(--text-dark)}
.about-title em{font-style:normal;color:var(--green-dark)}
.about-text{left:193px;top:674px;width:452px;font-family:"Roboto",sans-serif;font-size:9.6px;line-height:18.5px;color:var(--text-body)}
.read-more{left:194px;top:786px;font-family:"Roboto",sans-serif;font-size:10px;color:#5ea21c}
.about-photo{left:655px;top:644px;width:313px;height:159px;border:1px solid #ccc;background:linear-gradient(180deg,#3f7fc8 0%,#8bb7e3 55%,#b49a72 78%,#8c7256 100%)}

.section-title{font-family:"Roboto",sans-serif;font-size:14.5px;color:var(--green-dark)}
.cust-title{left:193px;top:842px}
.cust-sub{left:191px;top:866px;font-family:"Open Sans",sans-serif;font-size:10px;color:var(--text-muted)}
.avatar{left:194px;top:897px;width:65px;height:65px;border-radius:50%;border:3px solid #e3e3e3;background:radial-gradient(circle at 50% 45%,#d9b79a,#9cb77a 80%)}
.quote{left:274px;top:901px;width:410px;font-size:13.8px;line-height:18.6px;color:var(--text-body)}
.quote-tail{left:194px;top:972px;font-family:"Open Sans",sans-serif;font-style:italic;font-size:13px;color:var(--text-muted)}
.cite{left:194px;top:1005px;font-family:"Open Sans",sans-serif;font-size:10px;color:var(--text-muted)}
.cite b{font-weight:400;color:var(--orange)}
.pager{top:1039px;width:15px;height:14px;border-radius:3px;background:linear-gradient(#eee,#c9c9c9);border:1px solid #bbb}

.news-title{left:718px;top:863px}
.news-box{left:717px;top:894px;width:242px;height:90px;background:var(--panel-grey);border-radius:2px}
.news-box p{position:absolute;left:15px;top:18px;font-family:"Open Sans",sans-serif;font-size:10px;color:var(--text-muted)}
.news-input{position:absolute;left:17px;top:44px;width:151px;height:27px;background:var(--white);border:1px solid #d6d6d6;font-family:"Open Sans",sans-serif;font-size:10px;color:#999;padding:7px 8px}
.news-go{position:absolute;left:180px;top:44px;width:37px;height:27px;background:var(--orange);color:var(--white);font-family:"Open Sans",sans-serif;font-size:10px;text-align:center;line-height:27px}

.footer{left:0;top:1075px;width:1161px;height:125px;background:var(--footer-bg);border-top:6px solid var(--green-dark)}
.footer-links{position:absolute;left:194px;top:34px;font-size:9.5px;font-weight:700;color:var(--white)}
.copyright{position:absolute;left:194px;top:61px;font-size:9.5px;font-weight:700;color:var(--white)}
.social{position:absolute;left:865px;top:29px;display:flex;gap:4px}
.social span{width:17px;height:17px;border-radius:2px}
</style>
</head>
<body>
<div class="abs top-stripe"></div>
<header class="abs header"></header>
<div class="abs brand"><span class="brand-mark"></span>NORTHGATE RESOURCES</div>
<div class="abs phone">
  <svg width="18" height="20" viewBox="0 0 18 20"><path d="M13 2c-4 0-9 5-9 11 0 3 2 5 4 5" fill="none" stroke="#3a7d0f" stroke-width="2" stroke-linecap="round"/><path d="M11 1l4 2-2 3-3-2z" fill="#3a7d0f"/></svg>
  <span>Cell : 1300PLM456</span>
</div>

<nav class="abs nav">
  <a style="left:238px">HOME</a>
  <a style="left:320px">ABOUT US</a>
  <a style="left:421px">ACTIVE STATES</a>
  <a style="left:546px">LEASE/PURCHASEMINERALS</a>
  <a style="left:732px">CAREERS</a>
  <a style="left:831px">CONTACT US</a>
</nav>

<div class="abs hero" role="img" aria-label="Oil pumpjack and storage tanks in an open field at sunset"></div>
<div class="abs hero-shadow"></div>
<svg class="abs arrow" style="left:62px" width="28" height="46" viewBox="0 0 28 46"><path d="M24 3L5 23l19 20" fill="none" stroke="#eee" stroke-width="5"/><path d="M24 3L5 23l19 20" fill="none" stroke="#999" stroke-width="2"/></svg>
<svg class="abs arrow" style="left:1070px" width="28" height="46" viewBox="0 0 28 46"><path d="M4 3l19 20L4 43" fill="none" stroke="#eee" stroke-width="5"/><path d="M4 3l19 20L4 43" fill="none" stroke="#999" stroke-width="2"/></svg>

<form class="abs quick-contact">
  <h2>Quick Contact</h2>
  <div class="qc-rule"></div>
  <div class="field" style="top:72px">Name</div>
  <div class="field" style="top:112px">Email</div>
  <div class="field" style="top:156px">Mobile</div>
  <div class="send">Send</div>
</form>

<div class="abs dots"><span class="active"></span><span></span><span></span><span></span></div>

<h1 class="abs about-title">About <em>Northgate Resources</em></h1>
<p class="abs about-text">Lorem Ipsum is simply dummy text of the printing and typesetting industry. Lorem Ipsum has been the industry's standard dummy text ever since the 1500s, when an unknown printer took a galley of type and scrambled it to make a type specimen book. It has survived not only five centuries, but also the leap into electronic typesetting, remaining essentially unchanged. It was popularised in the 1960s with the release of Lettrafold sheets containing Lorem Ipsum passages, and more recently with desktop publishing software like Quill PageSetter including versions of Lorem Ipsum.</p>
<div class="abs read-more">Read More +</div>
<div class="abs about-photo" role="img" aria-label="Oil pumpjack and white storage tanks under a blue sky"></div>

<h2 class="abs section-title cust-title">What our Customers say</h2>
<div class="abs cust-sub">Lorem ipsum dolor sit amet, consectetuer adipiscing elit.</div>
<div class="abs avatar" role="img" aria-label="Portrait of the customer"></div>
<p class="abs quote">Ut wisi enim ad minim veniam, quis nostrud exerci tation ullam-corper. Lorem ipsum dolor sit amet, consectetuer adipiscing elit, sed diam nonummy nibh euismod tincidunt ut laoreet dolore magna aliquam erat volutpat.</p>
<div class="abs quote-tail">saepius.</div>
<div class="abs cite"><b>Colin Mercer</b>, ENT Department</div>
<div class="abs pager" style="left:272px"><svg width="13" height="12" viewBox="0 0 13 12"><path d="M8 3L5 6l3 3" fill="none" stroke="#666" stroke-width="1.5"/></svg></div>
<div class="abs pager" style="left:292px"><svg width="13" height="12" viewBox="0 0 13 12"><path d="M5 3l3 3-3 3" fill="none" stroke="#666" stroke-width="1.5"/></svg></div>

<h2 class="abs section-title news-title">News Letters</h2>
<div class="abs news-box">
  <p>Sign up out newsletter to get latest updates</p>
  <div class="news-input">Email Address</div>
  <div class="news-go">Go</div>
</div>

<footer class="abs footer">
  <div class="footer-links">Home | About | Practices | People | Events | Contact | Site Map | Privacy Policy</div>
  <div class="copyright">Copyright © 2014 Northgate. All Rights Reserved</div>
  <div class="social">
    <span style="background:#4a67b0"></span>
    <span style="background:#55a9dd"></span>
    <span style="background:#c8473a"></span>
    <span style="background:#c9314a"></span>
    <span style="background:#f2f2f2"></span>
  </div>
</footer>
</body>
</html>
```